Digital Media Services Brochure

There are four services Lumen offers; web design, email marketing, social media and search engine optimization (SEO)

For now, we are looking only to design the Web Design piece. It will be the first of 4 similar designs, so keep in mind the actual design work has to carry over to other pages and be cohesive.

Lumen offers 4 services and each service has its own color. We would like a graphic representing all four services with coordinating colors. Since we are doing the Web Design page right now, blue should be used throughout the piece to differentiate it as the Web Design marketing piece.

Services and colors:
• Web Design = blue
• Social Media = pink
• SEO = green
• Email = gray

Web Design: Front Page Includes

The Lumen Advantage
• Increase Revenue
• Look Professional
• Reduce Expenses
• Attract Talent
• Creative

An area for 2 image examples (screenshots of work)

Lumen Information
• Facebook Icon and “facebook.com/LumenKV”
• Twitter Icon and “@LumenKV”
• Website: lumenkv.example
• Phone Number: 555.214.7093

Web Design: Back Page Includes

What’s next?
• Design consult
• Content creation
• Optimization
• Test/launch
• Marketing

Space for a testimonial and a photo

Space for a small quote or random fact

We want to show off some of our current clients so it should say “Some of our stellar clients” then show four client logos that are attached.

Target Market(s)

Marketing Directors of medium sized businesses which undertand and appreciate the value of digital media and how it drives business today.

Industry/Entity Type

Marketing

Requirements
Must have
• Similar feel of the Lumen website: lumenkv.example but doesn't need to be exactly the same, we are looking for a new design after all.

Include:
Facebook Icon with facebook.com/LumenKV
Twitter Icon with @LumenKV
Website: lumenkv.example
Phone Number: 555.214.7093
Nice to have
• Fun, trendy and clean design integrating the four Lumen colors.

```html
<!DOCTYPE html>
<html lang="en">
<head>
<meta charset="utf-8">
<title>Lumen Web Design – What's next?</title>
<link href="https://fonts.googleapis.com/css2?family=Arimo:wght@400;700&display=swap" rel="stylesheet">
<style>
  :root {
    --web-blue: #1b7cc3;
    --text-blue: #1f80c4;
    --white: #ffffff;
    --ink: #2a2a2a;
    --green: #3aa64a;
  }
  * { margin: 0; padding: 0; box-sizing: border-box; }
  html, body { width: 927px; height: 1200px; overflow: hidden; background: var(--white); }
  body { font-family: "Arimo", Arial, sans-serif; }
  .page { position: relative; width: 927px; height: 1200px; overflow: hidden; background: var(--white); }

  .wave { position: absolute; left: 0; top: 0; width: 927px; height: 1200px; }

  .heading {
    position: absolute; left: 59px; top: 66px;
    font-size: 40px; font-weight: 700; color: var(--text-blue);
  }
  .steps {
    position: absolute; left: 86px; top: 164px; list-style: none;
    font-size: 29px; line-height: 38px; color: var(--text-blue);
  }
  .quote {
    position: absolute; left: 417px; width: 490px;
    font-size: 25px; line-height: 32px; color: var(--text-blue);
  }
  .quote cite { display: block; text-align: right; font-style: normal; padding-right: 8px; }
  .quote--one { top: 216px; }
  .quote--two { top: 364px; }

  .testimonial { position: absolute; left: 59px; width: 830px; display: flex; }
  .testimonial--one { top: 673px; }
  .testimonial--two { top: 839px; }
  .testimonial__photo { width: 134px; height: 134px; background: var(--white); flex: none; }
  .testimonial__body {
    margin-left: 34px; margin-top: 12px; flex: 1;
    font-size: 25px; line-height: 32px; color: var(--white);
  }
  .testimonial__body cite { display: block; text-align: right; font-style: normal; margin-top: 2px; }

  .clients-label {
    position: absolute; left: 59px; top: 1022px;
    font-size: 24px; color: var(--white);
  }
  .clients {
    position: absolute; left: 0; top: 1056px; width: 927px; height: 144px;
    background: var(--white); display: flex; align-items: center;
    padding-left: 56px; gap: 60px;
  }
  .client { display: flex; align-items: center; gap: 10px; font-size: 24px; font-weight: 700; color: var(--web-blue); }
  .client__mark { width: 18px; height: 18px; background: var(--web-blue); }
</style>
</head>
<body>
<main class="page">
  <svg class="wave" viewBox="0 0 927 1200" aria-hidden="true">
    <path d="M0 477 C 120 540, 300 585, 470 598 C 640 610, 800 630, 927 667 L 927 1056 L 0 1056 Z" fill="var(--web-blue)"/>
  </svg>

  <h1 class="heading">What’s next?</h1>
  <ul class="steps">
    <li>-Design Consult</li>
    <li>-Content Creation</li>
    <li>-Optimization</li>
    <li>-Test/Launch</li>
    <li>-Marketing</li>
  </ul>

  <blockquote class="quote quote--one">
    <p>“Social media isn’t a fad. It’s a fundamental shift in the way we communicate.”</p>
    <cite>-Social Current Media</cite>
  </blockquote>
  <blockquote class="quote quote--two">
    <p>“Social media isn’t a fad. It’s a fundamental shift in the way we communicate.”</p>
    <cite>-Social Current Media</cite>
  </blockquote>

  <section class="testimonial testimonial--one">
    <div class="testimonial__photo" role="img" aria-label="Client photo"></div>
    <blockquote class="testimonial__body">
      <p>“Testimonial from some of our clients will go in this space.”</p>
      <cite>-Client</cite>
    </blockquote>
  </section>
  <section class="testimonial testimonial--two">
    <div class="testimonial__photo" role="img" aria-label="Client photo"></div>
    <blockquote class="testimonial__body">
      <p>“Testimonial from some of our clients will go in this space.”</p>
      <cite>-Client</cite>
    </blockquote>
  </section>

  <p class="clients-label">Some of our stellar clients:</p>
  <div class="clients">
    <span class="client"><span class="client__mark"></span>Brookfield Rangers</span>
    <span class="client">Harlan Trophy</span>
    <span class="client">Vitalis Care</span>
  </div>
</main>
</body>
</html>
```